Etiketten - WINE LABEL for a natural wine
Zielgruppe
The family winery Lorenz Falkner stands for first-class wines from the Traisental and is considered to be one of the flagship wineries of the wine country Austria. The region's leading winery produces distinctive wines full of character on unique limestone conglomerate soils, with clear-as-a-bell stylistics and minerality accentuated by the terroir. Uncompromising work in the vineyard and cellar in favour of the highest quality is the highest premise of the Lorenz Falkner winery. In terms of a holistic understanding of nature, the vineyards are cultivated according to organic guidelines, and the entire winery is also certified according to the Grüne Rebe Standard standard. In addition to numerous national and international awards, Lorenz Falkner was named 'Vinoria Winemaker of the Year', the Oscar of the Austrian wine industry, at a young age. The wines of the Lorenz Falkner winery can be found in more than 35 nations worldwide, making the winery one of the most successful exporters of Austrian wines in the premium segment.
Our target group for this project are Natural Wine lovers. Natural wines are wines which don´t contain any additives, they are unfiltered(cloudy). Natural Wines have gained a lot of market share in the last years, the target group are people who like natural wine.
Aufgabenstellung
We are looking for a front label for our wine bottle. The bottle conists from white glas, the wine has an yellow-orange colour. The wine is cloudy. (picture of the bottle without labels in graphic atteched)
The brand name for this wine is WELLENSPIEL.
The maximum label dimensions can be 100 mm in height and 120 mm in width. Any size of the label within these parameters is possible.
The label can go in two directions.
Either a clear, reduced, minimalist design or a bolder, attention-grabbing more edgy design.
In both variants, the brand name WELLENSPIEL must be very clearly recognizable, as this creates the brand value of the product.

```html
<!DOCTYPE html>
<html lang="en">
<head>
<meta charset="utf-8">
<title>Wellenspiel – Natural Wine Label</title>
<link rel="stylesheet" href="https://fonts.googleapis.com/css2?family=Inter:wght@400&display=swap">
<style>
  :root {
    --backdrop: #e9e3da;
    --label-plum: #64144f;
    --label-ink: #ffffff;
  }
  html, body {
    margin: 0;
    padding: 0;
    width: 1200px;
    height: 1200px;
    overflow: hidden;
    background: var(--backdrop);
  }
  .canvas {
    position: relative;
    width: 1200px;
    height: 1200px;
  }
  .wine-label {
    position: absolute;
    left: 120px;
    top: 180px;
    width: 960px;
    height: 840px;
    background: var(--label-plum);
    color: var(--label-ink);
    font-family: "Inter", sans-serif;
    font-weight: 400;
    box-sizing: border-box;
  }
  .brand-name {
    position: absolute;
    left: 52px;
    top: 56px;
    margin: 0;
    font-family: "Inter", sans-serif;
    font-weight: 400;
    font-size: 100px;
    line-height: 1;
    letter-spacing: 2px;
    white-space: nowrap;
  }
  .wine-style {
    position: absolute;
    left: 690px;
    top: 500px;
    margin: 0;
    font-size: 44px;
    line-height: 1.05;
    letter-spacing: 3px;
  }
  .origin {
    position: absolute;
    left: 690px;
    top: 758px;
    display: flex;
    align-items: center;
    gap: 16px;
    font-size: 22px;
    letter-spacing: 3px;
  }
  .origin-mark {
    width: 26px;
    height: 18px;
    display: block;
  }
</style>
</head>
<body>
  <main class="canvas">
    <section class="wine-label">
      <h1 class="brand-name">WELLENSPIEL</h1>
      <p class="wine-style">NATURAL<br>WINE</p>
      <div class="origin">
        <svg class="origin-mark" viewBox="0 0 26 18" aria-hidden="true">
          <rect x="0" y="0" width="26" height="6" fill="#ffffff"/>
          <rect x="0" y="12" width="26" height="6" fill="#ffffff"/>
        </svg>
        <span>AUSTRIA</span>
      </div>
    </section>
  </main>
</body>
</html>
```